A5 8pp Brochure - all copy, images, rough layout supplied

A5 8pp Brochure (front/back cover and 6pp inside).
All copy and images supplied. Layout and image placement suggestions provided.

The focus for this brochure is about making custom made uniforms for dance studios. This brochure will be given to dance school owners.

They want to communicate the process and also the fact that dance schools can make money from on-selling the uniforms to their students, so an additional income stream for the school.

Simple colour palette mainly black, grey, white and purple. I imagine the images supplied will provide most of the colour/pop for the brochure. Please look at the website for basic look and feel. I have also attached a mocked up flyer to show you a style that we like.

All referenced files and images should be attached.

Just need someone to put it together beautifully for me.

Reason: Extending deadline for 2 days. All submissions needed by end of day Tuesday 1 Sept. Thank you.

Target Market(s)

Dance studio owners / teachers

Font styles to use
Serif
Sans Serif

Colors
876aae
886aae
b7a5cd
e4daeb
f3f1f8
000000
ffffff
848484

Requirements
Must have
• Images of the custom made uniforms

```html
<!DOCTYPE html>
<html lang="en">
<head>
<meta charset="utf-8">
<title>Design and Sample – Brochure Page</title>
<link rel="stylesheet" href="https://fonts.googleapis.com/css2?family=Arimo:wght@400;700&display=swap">
<style>
  :root {
    --purple: #886aae;
    --purple-deep: #6f4f9a;
    --lilac: #b7a5cd;
    --lavender: #e4daeb;
    --mist: #f3f1f8;
    --ink: #444444;
    --grey: #848484;
    --grey-light: #d9d9d9;
    --grey-pale: #ededed;
    --white: #ffffff;
  }
  * { margin: 0; padding: 0; box-sizing: border-box; }
  html, body { width: 847px; height: 1200px; overflow: hidden; background: var(--white); }
  body { font-family: "Arimo", Arial, sans-serif; color: var(--ink); }
  .page { position: relative; width: 847px; height: 1200px; overflow: hidden; background: var(--white); }

  .top-swoosh, .bottom-band { position: absolute; left: 0; width: 847px; }
  .top-swoosh { top: 0; height: 80px; }
  .bottom-band { bottom: 0; height: 150px; }

  .section-title {
    position: absolute; left: 93px;
    font-weight: 700; font-size: 26px; letter-spacing: 0.5px;
    color: var(--purple-deep);
  }
  .body-copy {
    position: absolute; left: 93px;
    font-size: 15.5px; line-height: 1.45; color: var(--grey);
  }
  .feature-list { position: absolute; left: 113px; list-style: none; }
  .feature-list li {
    position: relative; padding-left: 24px;
    font-size: 15.5px; line-height: 1.3; color: var(--grey);
  }
  .feature-list li::before {
    content: ""; position: absolute; left: 0; top: 6px;
    width: 8px; height: 8px; border-radius: 50%; background: var(--lilac);
  }

  .design-title { top: 132px; }
  .design-intro { top: 205px; width: 410px; }
  .design-lead { top: 325px; }
  .design-list { top: 365px; width: 420px; }

  .dancer-sketch {
    position: absolute; left: 555px; top: 195px; width: 200px; height: 390px;
    background: linear-gradient(180deg, var(--white) 0%, var(--mist) 50%, var(--white) 100%);
    border-radius: 90px 90px 60px 60px;
  }

  .sample-title { top: 618px; }
  .sample-intro { top: 690px; width: 410px; }

  .offer-box {
    position: absolute; left: 93px; top: 815px; width: 400px; height: 160px;
    background: linear-gradient(90deg, var(--grey-pale) 0%, var(--white) 100%);
  }
  .offer-lead { position: absolute; left: 107px; top: 827px; font-size: 18px; color: var(--ink); }
  .sample-list { top: 865px; width: 380px; }
  .sample-list li { margin-bottom: 8px; }

  .swatch-card {
    position: absolute; left: 523px; top: 665px; width: 245px; height: 340px;
    background: linear-gradient(160deg, #e6e6e6 0%, #cfcfcf 55%, #a8a0b4 100%);
    box-shadow: 2px 3px 6px rgba(0,0,0,0.15);
  }
</style>
</head>
<body>
<main class="page">
  <svg class="top-swoosh" viewBox="0 0 847 80" aria-hidden="true">
    <path d="M380 0 C560 50 720 55 847 12 L847 0 Z" fill="var(--grey-light)"/>
    <path d="M470 0 C620 38 740 40 847 5 L847 0 Z" fill="var(--lilac)"/>
    <path d="M560 0 C680 25 770 24 847 0 Z" fill="var(--purple)"/>
  </svg>

  <h2 class="section-title design-title">DESIGN</h2>
  <p class="body-copy design-intro">We offer guidance and advice to our customers by drawing on our&nbsp; fashion experiences.</p>
  <p class="body-copy design-lead">We offer the ability to:</p>
  <ul class="feature-list design-list">
    <li>Produce samples from photos and sketches alone</li>
    <li>Source suitable fabrics</li>
    <li>Vary price and quality depending on your requirements and budget</li>
    <li>Embroid and hand bead</li>
    <li>Develop exclusive designs and prints</li>
    <li>Print desired graphics using a variety of techniques</li>
  </ul>

  <div class="dancer-sketch" role="img" aria-label="Pencil fashion sketch of a dance costume"></div>

  <h2 class="section-title sample-title">SAMPLE</h2>
  <p class="body-copy sample-intro">Our expert team of technical designers, pattern makers and fabric sources transform designs to reality.</p>

  <div class="offer-box"></div>
  <p class="offer-lead">We offer:</p>
  <ul class="feature-list sample-list">
    <li>Technical change recommendations to improve garment production</li>
    <li>Fabric recommendations</li>
    <li>Fast sample production</li>
    <li>Free fit ammendments</li>
  </ul>

  <div class="swatch-card" role="img" aria-label="Fabric swatch card showing a grid of coloured fabric samples"></div>

  <svg class="bottom-band" viewBox="0 0 847 150" aria-hidden="true">
    <path d="M0 20 C250 0 600 0 847 18 L847 150 L0 150 Z" fill="var(--grey-pale)"/>
    <path d="M0 70 C300 55 600 55 847 72 L847 150 L0 150 Z" fill="var(--grey-light)"/>
  </svg>
</main>
</body>
</html>
```